Maple Crest Tutoring General Flyer Design

Reason: We are very close to making a selection but would like to provide a little more time for some of the designers to complete their revisions.
Target Market(s)
Secondary school students
Industry/Entity Type
Education
Requirements
Must have
- company logo and company name (see attached file)

```html
<!DOCTYPE html>
<html lang="en">
<head>
<meta charset="utf-8">
<title>Maple Crest Tutoring – Flyer</title>
<link rel="stylesheet" href="https://fonts.googleapis.com/css2?family=Montserrat:wght@300;800&family=Open+Sans:wght@400;700;800&family=Oswald:wght@600;700&display=swap">
<style>
  :root {
    --red: #e8202a;
    --maroon: #8c2a35;
    --deep-maroon: #7a1f2a;
    --white: #ffffff;
    --shadow: #2a1418;
    --ink-red: #9b2430;
  }
  html, body {
    margin: 0;
    padding: 0;
    overflow: hidden;
    background: var(--white);
  }
  .flyer {
    position: relative;
    width: 776px;
    height: 1200px;
    overflow: hidden;
    background: var(--white);
    font-family: "Open Sans", Arial, sans-serif;
  }
  .hero-photo {
    position: absolute;
    left: 0; top: 0;
    width: 776px; height: 530px;
    background:
      linear-gradient(to bottom, rgba(255,255,255,0) 55%, var(--white) 98%),
      linear-gradient(100deg, #6d7f9a 0%, #8aa1b9 25%, #b7b4aa 45%, #6f9a48 70%, #4c7d2c 100%);
  }
  .headline {
    position: absolute;
    right: 56px;
    top: 434px;
    margin: 0;
    text-align: right;
    font-family: "Montserrat", Arial, sans-serif;
    font-weight: 800;
    color: var(--red);
    font-size: 86px;
    line-height: 98px;
    letter-spacing: 3px;
  }
  .tagline {
    position: absolute;
    right: 56px;
    top: 614px;
    margin: 0;
    font-family: "Montserrat", Arial, sans-serif;
    font-weight: 300;
    color: var(--ink-red);
    font-size: 55px;
    line-height: 64px;
    letter-spacing: 1px;
  }
  .brand {
    position: absolute;
    left: 36px;
    top: 680px;
    width: 290px;
    text-align: center;
  }
  .brand-mark {
    display: block;
    width: 30px; height: 30px;
    margin: 0 auto 36px;
    background: var(--deep-maroon);
  }
  .brand-name {
    display: block;
    white-space: nowrap;
    font-family: "Oswald", Arial, sans-serif;
    font-weight: 700;
    font-size: 24px;
    line-height: 30px;
    color: var(--deep-maroon);
    text-transform: uppercase;
    letter-spacing: 0.3px;
  }
  .exams-title {
    position: absolute;
    right: 58px;
    top: 700px;
    margin: 0;
    font-weight: 800;
    font-size: 27px;
    color: var(--maroon);
  }
  .exam-list {
    position: absolute;
    left: 358px;
    top: 752px;
    width: 366px;
    margin: 0; padding: 0;
    list-style: none;
    display: grid;
    grid-template-columns: 170px 170px;
    column-gap: 20px;
    row-gap: 21px;
  }
  .exam {
    height: 60px;
    background: var(--red);
    color: var(--white);
    font-weight: 700;
    font-size: 38px;
    line-height: 60px;
    text-align: center;
    box-shadow: 4px 4px 0 var(--shadow);
  }
  .corner-shapes {
    position: absolute;
    left: 0; top: 0;
  }
  .trial-badge {
    position: absolute;
    left: 40px;
    top: 875px;
    width: 250px;
    height: 250px;
  }
  .badge-text {
    position: absolute;
    left: 40px; top: 875px;
    width: 250px;
    text-align: center;
    color: var(--white);
  }
  .badge-lead {
    margin: 30px 0 0;
    font-weight: 800;
    font-size: 19px;
    line-height: 24px;
  }
  .badge-free {
    margin: -4px 0 0;
    font-family: "Oswald", Arial, sans-serif;
    font-weight: 700;
    font-size: 80px;
    line-height: 80px;
  }
  .badge-offer {
    margin: -2px 0 0;
    font-family: "Oswald", Arial, sans-serif;
    font-weight: 700;
    font-size: 31px;
    line-height: 34px;
  }
  .badge-call {
    margin: 0;
    font-weight: 800;
    font-size: 17px;
    line-height: 20px;
  }
  .contact {
    position: absolute;
    right: 56px;
    top: 985px;
    margin: 0;
    font-style: normal;
    text-align: right;
    color: var(--white);
    font-size: 18px;
    line-height: 19.5px;
  }
  .contact strong { font-weight: 700; }
  .contact .web {
    display: block;
    margin-top: 20px;
    font-weight: 700;
    font-size: 19px;
  }
</style>
</head>
<body>
<main class="flyer">
  <div class="hero-photo" role="img" aria-label="Photo of cheerful secondary school students sitting on outdoor steps, tossing notebooks into the air, trees behind them"></div>

  <h1 class="headline">COME OUT<br>ON TOP</h1>
  <p class="tagline">WE CAN HELP</p>

  <div class="brand">
    <span class="brand-mark"></span>
    <span class="brand-name">Maple Crest Tutoring</span>
  </div>

  <h2 class="exams-title">Exams we cover</h2>
  <ul class="exam-list">
    <li class="exam">MCT</li>
    <li class="exam">PMCT</li>
    <li class="exam">SMCT</li>
    <li class="exam">OSMCT</li>
  </ul>

  <svg class="corner-shapes" width="776" height="1200" viewBox="0 0 776 1200" aria-hidden="true">
    <polygon points="0,780 462,958 172,1200 0,1200" fill="var(--red)"/>
    <polygon points="500,955 776,955 776,1200 214,1200" fill="var(--maroon)"/>
  </svg>

  <svg class="trial-badge" viewBox="-125 -125 250 250" aria-hidden="true">
    <defs>
      <radialGradient id="badgeFill" cx="0.35" cy="0.3" r="0.8">
        <stop offset="0" stop-color="#f04048"/>
        <stop offset="1" stop-color="#b81a24"/>
      </radialGradient>
    </defs>
    <polygon fill="var(--white)" points="125,0 110.7,17.5 118.9,38.6 99.8,50.8 101.1,73.5 79.2,79.2 73.5,101.1 50.8,99.8 38.6,118.9 17.5,110.7 0,125 -17.5,110.7 -38.6,118.9 -50.8,99.8 -73.5,101.1 -79.2,79.2 -101.1,73.5 -99.8,50.8 -118.9,38.6 -110.7,17.5 -125,0 -110.7,-17.5 -118.9,-38.6 -99.8,-50.8 -101.1,-73.5 -79.2,-79.2 -73.5,-101.1 -50.8,-99.8 -38.6,-118.9 -17.5,-110.7 0,-125 17.5,-110.7 38.6,-118.9 50.8,-99.8 73.5,-101.1 79.2,-79.2 101.1,-73.5 99.8,-50.8 118.9,-38.6 110.7,-17.5"/>
    <polygon fill="var(--deep-maroon)" transform="scale(0.94)" points="125,0 110.7,17.5 118.9,38.6 99.8,50.8 101.1,73.5 79.2,79.2 73.5,101.1 50.8,99.8 38.6,118.9 17.5,110.7 0,125 -17.5,110.7 -38.6,118.9 -50.8,99.8 -73.5,101.1 -79.2,79.2 -101.1,73.5 -99.8,50.8 -118.9,38.6 -110.7,17.5 -125,0 -110.7,-17.5 -118.9,-38.6 -99.8,-50.8 -101.1,-73.5 -79.2,-79.2 -73.5,-101.1 -50.8,-99.8 -38.6,-118.9 -17.5,-110.7 0,-125 17.5,-110.7 38.6,-118.9 50.8,-99.8 73.5,-101.1 79.2,-79.2 101.1,-73.5 99.8,-50.8 118.9,-38.6 110.7,-17.5"/>
    <circle r="100" fill="url(#badgeFill)"/>
  </svg>
  <div class="badge-text">
    <p class="badge-lead">Try us out</p>
    <p class="badge-free">FREE</p>
    <p class="badge-offer">TRIAL LESSON</p>
    <p class="badge-call">Call or email us<br>today</p>
  </div>

  <address class="contact">
    4170 Birchmount Avenue,<br>
    Unit 310 Markham,<br>
    ON L3R 7K2<br>
    <strong>Email</strong><br>
    Hello@MapleCrestTutoring.com<br>
    <strong>Tel</strong><br>
    647-555-0184
    <span class="web">www.MapleCrestTutoring.com</span>
  </address>
</main>
</body>
</html>
```